Ironpeak MMA - Ironpeak Path - 7-5-4

This will be for a wall logo. Probably printed on vinyl to adhere to the wall. This a rough draft concept of the project, but we're certainly open to other designs. Red, Black and White are the main colors we would like to use. The triangle motif is important, it denotes stability and base, which are important in jiu jistu.
The Ironpeak Path (7-5-4)
7 Virtues of a Warrior (Bushido)
R Rectitude
Doing what is right w/o regard for the consequences
C Courage
Inner strength to resist opposition. Courage not just to step on the mat but to make the right decisions
B Benevolence
Mindset to do good. Be kind and generous
P Politeness
Proper consideration and courtesy to others
L Loyalty
Faithfulness & Alliance. Not blind allegiance
H Honesty / Sincerity
Be a man of your word. Do what you say you will
Genuine Integrity in character & action
H Honor
Profound respect & ethical conduct
Make the right decisions to be worthy of respectability
5 Keys to Health
Nutrition - Eat sensibly
Exercise - Stay fit and ready
Rest - Recovery and Recharge
Hygiene - Stay Clean
Attitude - Assume positive intent
Look at life in a positive way
4 States of Mind (Spirit of Budo)
Shoshin - Beginners Mind
Be open to new ideas
Eager to Learn
Zanshin – Remaining Mind
Being Alert and Aware, but relaxed
Be Prepared
Mushin – No Mind (Clear Mind)
Be able to act in the moment without having to think
Fudoshin – Immovable Mind
Emotional Balance
Free from anger, fear, & doubt

```html
<!DOCTYPE html>
<html lang="en">
<head>
<meta charset="utf-8">
<title>The Ironpeak Path (7-5-4)</title>
<link rel="stylesheet" href="https://fonts.googleapis.com/css2?family=Lobster&family=Anton&family=Montserrat:wght@500;600;700;800&display=swap">
<style>
  :root {
    --ink: #161514;
    --red: #d20a0a;
    --white: #ffffff;
    --muted: #e9e9e9;
    --photo-dark: #262424;
    --photo-warm: #5a1c1c;
  }
  * { margin: 0; padding: 0; box-sizing: border-box; }
  html, body { width: 731px; height: 1200px; overflow: hidden; background: var(--ink); }
  .poster {
    position: relative;
    width: 731px; height: 1200px;
    background: var(--ink);
    color: var(--white);
    font-family: "Montserrat", Arial, sans-serif;
    overflow: hidden;
  }
  .abs { position: absolute; }

  .triangle-motif { position: absolute; left: 0; top: 0; width: 731px; height: 1200px; }

  .fighters-photo {
    position: absolute;
    left: 300px; top: 462px;
    width: 431px; height: 478px;
    border-radius: 46% 0 40% 38% / 38% 0 44% 30%;
    background: radial-gradient(ellipse at 55% 55%, var(--photo-warm) 0%, var(--photo-dark) 70%);
  }

  .title {
    left: 57px; top: 40px;
    font-family: "Lobster", cursive;
    font-size: 56px;
    line-height: 1;
    white-space: nowrap;
  }
  .title .code {
    font-family: "Montserrat", Arial, sans-serif;
    font-weight: 800;
    font-size: 34px;
    color: var(--red);
    margin-left: 14px;
  }

  .section-head {
    font-family: "Montserrat", Arial, sans-serif;
    font-weight: 800;
    text-transform: uppercase;
    color: var(--red);
    line-height: 1;
  }
  .section-head .num { color: var(--white); }
  .virtues-head { left: 57px; top: 172px; font-size: 30px; }

  .virtue { position: absolute; width: 215px; }
  .virtue h3 {
    font-family: "Anton", Impact, sans-serif;
    font-weight: 400;
    font-size: 27px;
    line-height: 1.05;
    text-transform: uppercase;
    letter-spacing: 0.3px;
  }
  .virtue h3 .initial { color: var(--red); font-size: 33px; margin-right: 4px; }
  .virtue p {
    margin-top: 6px;
    font-size: 11.5px;
    font-weight: 500;
    line-height: 1.2;
    color: var(--muted);
  }
  .v-rectitude   { left: 57px;  top: 240px; }
  .v-courage     { left: 272px; top: 240px; }
  .v-benevolence { left: 57px;  top: 360px; }
  .v-politeness  { left: 272px; top: 366px; }
  .v-loyalty     { left: 57px;  top: 472px; }
  .v-honesty     { left: 57px;  top: 576px; width: 240px; }
  .v-honor       { left: 57px;  top: 704px; }

  .health-head { left: 57px; top: 930px; font-size: 32px; line-height: 1.05; }
  .states-head { left: 372px; top: 978px; font-size: 30px; }

  .checklist { list-style: none; position: absolute; }
  .checklist li { display: flex; align-items: center; white-space: nowrap; }
  .checklist svg { width: 13px; height: 13px; flex: none; margin-right: 11px; }
  .checklist strong { font-weight: 800; text-transform: uppercase; }

  .health-list { left: 60px; top: 1021px; font-size: 13px; font-weight: 600; }
  .health-list li { height: 23.5px; }
  .states-list { left: 380px; top: 1044px; font-size: 15.5px; font-weight: 800; text-transform: uppercase; }
  .states-list li { height: 34px; }

  .tagline { left: 57px; top: 1150px; font-size: 19px; font-weight: 600; }
</style>
</head>
<body>
<main class="poster">

  <svg class="triangle-motif" viewBox="0 0 731 1200" aria-hidden="true">
    <polygon points="587,232 246,922 930,922" fill="var(--white)"/>
    <polygon points="587,280 284,898 890,898" fill="var(--red)"/>
  </svg>

  <div class="fighters-photo" role="img" aria-label="Photo of two grapplers in black and red rash guards training jiu-jitsu, seen from above"></div>

  <h1 class="abs title">The Ironpeak Path<span class="code">(7-5-4)</span></h1>

  <h2 class="abs section-head virtues-head"><span class="num">7</span> Virtues of a Warrior</h2>

  <section class="virtue v-rectitude">
    <h3><span class="initial">R</span>Rectitude</h3>
    <p>Doing what is right w/o<br>regard for the consequences</p>
  </section>
  <section class="virtue v-courage">
    <h3><span class="initial">C</span>Courage</h3>
    <p>Inner strength to resist<br>opposition. Courage not just to<br>step on the mat but to<br>make the right decisions</p>
  </section>
  <section class="virtue v-benevolence">
    <h3><span class="initial">B</span>Benevolence</h3>
    <p>Mindset to do good. Be kind<br>and generous</p>
  </section>
  <section class="virtue v-politeness">
    <h3><span class="initial">P</span>Politeness</h3>
    <p>Proper consideration<br>and courtesy to others</p>
  </section>
  <section class="virtue v-loyalty">
    <h3><span class="initial">L</span>Loyalty</h3>
    <p>Faithfulness &amp; Alliance.<br>Not blind allegiance</p>
  </section>
  <section class="virtue v-honesty">
    <h3><span class="initial">H</span>Honesty / <span class="initial">S</span>incerity</h3>
    <p>Be a man of your word. Do what<br>you say you will. Genuine Integrity in<br>character &amp; action</p>
  </section>
  <section class="virtue v-honor">
    <h3><span class="initial">H</span>Honor</h3>
    <p>Profound respect &amp; ethical<br>conduct. Make the right decisions to<br>be worthy of respectability</p>
  </section>

  <svg width="0" height="0" style="position:absolute">
    <defs>
      <symbol id="tick" viewBox="0 0 16 16">
        <circle cx="8" cy="8" r="8" fill="var(--red)"/>
        <path d="M4.3 8.3 L7 11 L11.8 5.6" fill="none" stroke="var(--white)" stroke-width="2" stroke-linecap="round" stroke-linejoin="round"/>
      </symbol>
    </defs>
  </svg>

  <h2 class="abs section-head health-head"><span class="num">5</span> Keys<br>to Health</h2>
  <ul class="checklist health-list">
    <li><svg><use href="#tick"/></svg><span><strong>Nutrition</strong> - Eat sensibly</span></li>
    <li><svg><use href="#tick"/></svg><span><strong>Exercise</strong> - Stay fit and ready</span></li>
    <li><svg><use href="#tick"/></svg><span><strong>Rest</strong> - Recovery and Recharge</span></li>
    <li><svg><use href="#tick"/></svg><span><strong>Hygiene</strong> - Stay Clean</span></li>
    <li><svg><use href="#tick"/></svg><span><strong>Attitude</strong> - Assume positive intent</span></li>
  </ul>
  <p class="abs tagline">Look at life in a positive way</p>

  <h2 class="abs section-head states-head"><span class="num">4</span> States of Mind</h2>
  <ul class="checklist states-list">
    <li><svg><use href="#tick"/></svg><span>Shoshin - Beginners Mind</span></li>
    <li><svg><use href="#tick"/></svg><span>Zanshin – Remaining Mind</span></li>
    <li><svg><use href="#tick"/></svg><span>Mushin – No Mind</span></li>
    <li><svg><use href="#tick"/></svg><span>Fudoshin – Immovable Mind</span></li>
  </ul>

</main>
</body>
</html>
```